New Innovative Counselling and psychotherapy Service needs Business Card design

Keep it simple and professional. On one side, just company name and logo (perhaps in all blue) and maybe a tag line.

On other side (all white) my name and Qualifications in centre

Industry/Entity Type

Health And Wellness

Contact Information for Business Card

Derek Hollis
Counsellor & Psychotherapist
BSc (Psychol.), BA, Dip. (Couns. & Psych.), PG.Cert (CBT), MGVrA, NWTF

I will also require Mobile no, Email and web site address of which I'll pass on to final designer.

Font styles to use
Sans Serif

Requirements
Must have
• My Logo Only and please use the colours in logo that is in it.
Should not have
• Any other images

```html
<!DOCTYPE html>
<html lang="en">
<head>
<meta charset="utf-8">
<title>Calder Path – Business Card</title>
<link rel="stylesheet" href="https://fonts.googleapis.com/css2?family=Lato:wght@400;700;900&family=Montserrat:wght@400&display=swap">
<style>
  :root {
    --backdrop: #2b2b2b;
    --card: #ffffff;
    --ink: #1e1e1e;
    --brand-blue: #45b0e5;
    --wordmark: #2a2a2a;
  }
  * { margin: 0; padding: 0; box-sizing: border-box; }
  html, body {
    width: 1200px;
    height: 900px;
    overflow: hidden;
    background: var(--backdrop);
  }
  .canvas {
    width: 1200px;
    height: 900px;
    display: flex;
    flex-direction: column;
    align-items: center;
    justify-content: center;
    gap: 52px;
  }
  .card {
    width: 630px;
    height: 360px;
    background: var(--card);
    border-radius: 18px;
    display: flex;
    flex-direction: column;
    align-items: center;
    justify-content: center;
    font-family: "Lato", sans-serif;
  }

  /* Front */
  .brand {
    display: flex;
    align-items: center;
    gap: 16px;
  }
  .brand-dot {
    width: 44px;
    height: 44px;
    border-radius: 50%;
    background: var(--brand-blue);
  }
  .brand-name {
    font-family: "Montserrat", sans-serif;
    font-weight: 400;
    font-size: 36px;
    color: var(--wordmark);
    letter-spacing: 0.2px;
  }
  .tagline {
    margin-top: 26px;
    font-size: 12px;
    font-weight: 400;
    letter-spacing: 5px;
    color: var(--brand-blue);
    text-transform: uppercase;
  }

  /* Back */
  .holder-name {
    font-size: 24px;
    font-weight: 900;
    letter-spacing: 3px;
    color: var(--brand-blue);
    text-transform: uppercase;
  }
  .role-row {
    display: flex;
    align-items: center;
    gap: 6px;
    margin-top: 4px;
  }
  .rule {
    width: 150px;
    height: 2px;
    background: var(--ink);
  }
  .role {
    font-size: 13px;
    font-weight: 700;
    color: var(--ink);
  }
  .qualifications {
    margin-top: 30px;
    font-size: 14px;
    font-weight: 400;
    color: var(--ink);
    text-transform: uppercase;
    letter-spacing: 0.2px;
  }
</style>
</head>
<body>
  <main class="canvas">
    <section class="card card-front">
      <div class="brand">
        <span class="brand-dot"></span>
        <span class="brand-name">Calder Path</span>
      </div>
      <p class="tagline">Moving gently into wellbeing</p>
    </section>

    <section class="card card-back">
      <h1 class="holder-name">Derek Hollis</h1>
      <div class="role-row">
        <span class="rule"></span>
        <span class="role">Counsellor &amp; Psychotherapist</span>
        <span class="rule"></span>
      </div>
      <p class="qualifications">BSc (Psychol.), BA, Dip. (Couns. &amp; Psych.), PG.Cert (CBT), MGVrA, NWTF</p>
    </section>
  </main>
</body>
</html>
```